Wordpress Website for electrician

I'm looking for an easy to maintain website for my electrical contracting business. Need a professional and appealing site.
Im wanting a website where clients can come on and look at services we offer, case studies and advertise our services.
Colours I'm wanting to incorporate are green, white, black and grey
I'm wanting a big slide show on main page where I can place advertising etc.
Menu is to include home, services, our work, specials, energy efficiency and contact
My existing site is www.brivolelectric.com.au
looking for something with a similar layout to this website
Target Market(s)
Businesses
Industry/Entity Type
Electrician
Look and feel

```html
<!DOCTYPE html>
<html lang="en">
<head>
<meta charset="utf-8">
<title>Brivol Electric – Electrical Contractor</title>
<link href="https://fonts.googleapis.com/css2?family=PT+Sans:wght@400;700&family=Open+Sans:wght@400;600;700;800&display=swap" rel="stylesheet">
<style>
:root{
  --green:#3aa648;
  --green-dark:#2f9a3e;
  --green-light:#7ccf86;
  --black:#231f20;
  --grey-band:#ececec;
  --grey-line:#d9d9d9;
  --grey-box:#efefef;
  --text:#1b1b1b;
  --white:#ffffff;
}
*{box-sizing:border-box;margin:0;padding:0}
html,body{width:1200px;height:1000px;overflow:hidden;background:var(--white);font-family:"Open Sans",Arial,sans-serif;color:var(--text)}
.band{position:absolute;left:181px;top:0;width:837px;height:1000px;background:var(--grey-band)}
.phone{position:absolute;left:742px;top:8px;display:flex;align-items:center;gap:8px;color:var(--green);font:700 24px "Open Sans",sans-serif;letter-spacing:1px}
.page{position:absolute;left:272px;top:44px;width:654px;height:944px;background:var(--white);box-shadow:4px 6px 8px rgba(0,0,0,.35)}
.abs{position:absolute}
.brand{left:14px;top:22px;display:flex;align-items:center;gap:10px}
.brand-dot{width:40px;height:40px;border-radius:50%;background:var(--green)}
.brand-name{font:700 30px "PT Sans",sans-serif;color:var(--black);line-height:1}
.brand-tag{left:118px;top:54px;font-size:10px;color:#666;letter-spacing:.5px}
.search{left:470px;top:30px;width:176px;height:28px;border:2px solid #cfcfcf;border-radius:6px;background:#f2f2f2;box-shadow:inset 0 1px 2px rgba(0,0,0,.2)}
.search svg{position:absolute;right:6px;top:4px}
.nav{left:7px;top:94px;width:640px;height:32px;background:var(--black);border-radius:3px;display:flex}
.nav a{color:#eee;font-size:9.5px;text-decoration:none;padding:0 18px;line-height:32px;border-right:1px solid #444}
.hero{left:7px;top:131px;width:640px;height:226px;background:linear-gradient(160deg,#3a2a4a 0%,#7a4fa0 25%,#2d2a2c 50%,#6b5a3e 80%,#1e1b1c 100%)}
.hero-caption{position:absolute;right:0;bottom:0;width:171px;height:97px;background:rgba(40,40,40,.75);color:#fff;font:300 32px/38px "Open Sans",sans-serif;padding:10px 0 0 30px;letter-spacing:-.5px}
.service{left:7px;width:413px;height:70px;border:1px solid #e2e2e2;border-radius:4px;box-shadow:0 1px 2px rgba(0,0,0,.08)}
.service-icon{position:absolute;left:0;top:0;width:68px;height:70px;background:var(--black);border-radius:4px 0 0 4px;display:flex;align-items:center;justify-content:center}
.service h2{position:absolute;left:99px;top:9px;font:400 19px "PT Sans",sans-serif;color:#111}
.service p{position:absolute;left:99px;top:38px;width:225px;font-size:8.5px;line-height:12px}
.service .arrow{position:absolute;left:370px;top:27px}
.ad-green{left:450px;top:370px;width:198px;height:162px;border:1px solid #ddd;overflow:hidden}
.ad-bulb{position:absolute;left:70px;top:4px;width:56px;height:54px;border-radius:50%;background:radial-gradient(#d8e8c8,#9ab08a 60%,#ffffff 72%)}
.ad-green .l1{position:absolute;left:0;width:100%;top:56px;text-align:center;font:800 33px "Open Sans",sans-serif;color:var(--green);letter-spacing:-1px}
.ad-green .l2{position:absolute;left:0;width:100%;top:90px;text-align:center;font:800 23px "Open Sans",sans-serif;color:#111;letter-spacing:-.5px}
.ad-grass{position:absolute;left:0;bottom:0;width:100%;height:22px;background:linear-gradient(#8fd070,#3c8a2c)}
.ad-led{left:450px;top:542px;width:198px;height:86px;border:1px solid #ddd}
.ad-box{position:absolute;left:16px;top:8px;width:50px;height:60px;background:linear-gradient(135deg,#d7c9ea,#7d4fb0)}
.ad-led .cond{position:absolute;left:20px;top:71px;font-size:5px;font-weight:700}
.ad-led .t1{position:absolute;left:68px;top:4px;font:800 13px "Open Sans",sans-serif;color:var(--green)}
.ad-led .t2{position:absolute;left:90px;top:18px;font:700 6.5px "Open Sans",sans-serif}
.ad-led .price{position:absolute;left:90px;top:28px;font:800 30px "Open Sans",sans-serif;color:var(--green-light)}
.ad-led .each{position:absolute;left:153px;top:36px;font:700 6px "Open Sans",sans-serif;color:var(--green-light)}
.ad-led .more{position:absolute;left:83px;top:70px;font:600 6.5px "Open Sans",sans-serif;color:#f0b43c}
.widget{left:465px;width:166px;height:117px;border:2px solid var(--green-dark)}
.widget h3{position:absolute;left:18px;top:6px;width:126px;text-align:center;font:400 15px "PT Sans",sans-serif;padding-bottom:6px;border-bottom:1px solid #ccc}
.widget h4{position:absolute;left:20px;top:42px;font:700 8.5px "Open Sans",sans-serif;color:var(--green)}
.widget p{position:absolute;left:20px;top:53px;width:128px;font-size:8.5px;line-height:12px}
.widget .all{position:absolute;left:0;bottom:0;width:100%;height:17px;background:var(--green-dark);color:#fff;text-align:center;font-size:10px;line-height:17px}
.col{top:641px;font-size:8.5px;line-height:12px}
.col h2{font:400 14.5px/20px "PT Sans",sans-serif;color:#111;text-transform:uppercase}
.col-left{left:16px;width:190px}
.col-left p{margin-top:32px}
.col-right{left:239px;width:184px}
.col-right p{margin-top:11px}
.divider{left:218px;top:642px;width:1px;height:130px;background:var(--grey-line)}
.quote{left:7px;top:796px;width:413px;height:71px;background:var(--grey-box);border-radius:4px}
.quote svg{position:absolute;left:12px;top:16px}
.quote p{position:absolute;left:51px;top:16px;width:320px;font-size:8.5px;line-height:12px}
.quote cite{position:absolute;right:50px;top:40px;font-size:8.5px;font-style:normal;font-weight:700}
.quote cite span{color:var(--green-dark);font-weight:400}
.foot-line{left:7px;top:885px;width:640px;height:1px;background:var(--grey-line)}
.foot-links{left:0;top:904px;width:654px;text-align:center;font-size:7.5px;font-weight:700;color:var(--green-dark)}
.foot-links span{color:#777;font-weight:400;margin:0 3px}
.copy{left:0;top:918px;width:654px;text-align:center;font-size:7.5px;color:#444}
.copy a{color:var(--green-dark);text-decoration:none}
</style>
</head>
<body>
<div class="band"></div>
<div class="phone">
  <svg width="34" height="26" viewBox="0 0 34 26"><path d="M2 9c0-5 30-5 30 0v3h-7V8H9v4H2z" fill="#555"/><path d="M7 12h20l4 12H3z" fill="#555"/><circle cx="17" cy="18" r="4" fill="var(--grey-band)"/></svg>
  0400 555 018
</div>
<main class="page">
  <div class="abs brand"><div class="brand-dot"></div><div class="brand-name">Brivol Electric</div></div>
  <div class="abs brand-tag">electrical contractor</div>
  <div class="abs search"><svg width="18" height="18" viewBox="0 0 18 18"><circle cx="7" cy="7" r="5.5" fill="none" stroke="#111" stroke-width="2"/><path d="M11 11l6 6" stroke="#111" stroke-width="2.5"/></svg></div>
  <nav class="abs nav"><a>Home</a><a>About</a><a>Services</a><a>Our Work</a><a>Specials</a><a>Energy Efficiency</a><a style="border:none">Contact</a></nav>
  <section class="abs hero" role="img" aria-label="Night photo of a lit modern terminal canopy with purple lights">
    <div class="hero-caption">Energy<br>Efficient</div>
  </section>

  <article class="abs service" style="top:369px">
    <div class="service-icon"><svg width="24" height="36" viewBox="0 0 24 36"><path d="M4 2v12a8 8 0 0 0 16 0V2M12 22v12" fill="none" stroke="var(--green)" stroke-width="4" stroke-linecap="round"/><path d="M12 4v12" stroke="var(--green)" stroke-width="4" stroke-linecap="round"/></svg></div>
    <h2>Electrical Contracting</h2>
    <p>We offer all types of electrical work from Installation to maintenance</p>
    <svg class="arrow" width="12" height="16" viewBox="0 0 12 16"><path d="M2 2l7 6-7 6" fill="none" stroke="var(--green)" stroke-width="3.5"/></svg>
  </article>
  <article class="abs service" style="top:450px">
    <div class="service-icon"><svg width="28" height="40" viewBox="0 0 28 40"><path d="M14 2a12 12 0 0 1 7 22v5H7v-5A12 12 0 0 1 14 2z" fill="var(--green)" stroke="#fff" stroke-width="2"/><rect x="8" y="31" width="12" height="6" rx="2" fill="var(--green)" stroke="#fff" stroke-width="2"/></svg></div>
    <h2>Energy Efficiency</h2>
    <p>With one of our audits to your business or home we can lower your energy bills and minimise your carbon footprint.</p>
    <svg class="arrow" width="12" height="16" viewBox="0 0 12 16"><path d="M2 2l7 6-7 6" fill="none" stroke="var(--green)" stroke-width="3.5"/></svg>
  </article>
  <article class="abs service" style="top:532px">
    <div class="service-icon"><svg width="50" height="40" viewBox="0 0 50 40"><path d="M6 30a19 19 0 0 1 38 0z" fill="var(--green)" stroke="#fff" stroke-width="2"/><path d="M2 30h46v5H2z" fill="var(--green)" stroke="#fff" stroke-width="2"/><circle cx="25" cy="22" r="5" fill="#fff"/></svg></div>
    <h2>Underground Locating</h2>
    <p>We have the tools and knowledge in locating underground utilities.</p>
    <svg class="arrow" width="12" height="16" viewBox="0 0 12 16"><path d="M2 2l7 6-7 6" fill="none" stroke="var(--green)" stroke-width="3.5"/></svg>
  </article>

  <aside class="abs ad-green">
    <div class="ad-bulb" role="img" aria-label="Light bulb with a small tree inside"></div>
    <div class="l1">BE GREEN</div>
    <div class="l2">SAVE MONEY</div>
    <div class="ad-grass" role="img" aria-label="Strip of green grass"></div>
  </aside>
  <aside class="abs ad-led">
    <div class="ad-box" role="img" aria-label="Boxed LED downlight product"></div>
    <div class="cond">CONDITIONS APPLY</div>
    <div class="t1">LED DOWNLIGHTS</div>
    <div class="t2">Supplied &amp; Installed</div>
    <div class="price">$33</div>
    <div class="each">EACH</div>
    <div class="more">Click here for more details</div>
  </aside>

  <section class="abs widget" style="top:636px">
    <h3>News</h3>
    <h4>ELECTRICITY PRICES TO SOAR</h4>
    <p>The Australian government's carbon tax will see electricity prices soar .</p>
    <div class="all">See all</div>
  </section>
  <section class="abs widget" style="top:761px">
    <h3>Specials</h3>
    <h4>COOLWAVE SPLIT SYSTEM</h4>
    <p>Beat the heat this summer! We can supply and install a new split system.</p>
    <div class="all">See all</div>
  </section>

  <section class="abs col col-left">
    <h2>LED is the future</h2>
    <p>LED lighting has involved rapidly in the last 5 years. In the coming years we will see all lighting being substitued with LED lights. It is by far the most efficient form of lighting on todays market. Let us retrofit your business or home with LED and the savings will literally pay the lights off.</p>
  </section>
  <div class="abs divider"></div>
  <section class="abs col col-right">
    <h2>Reduce your business energy consumption</h2>
    <p>By letting us analyse your energy consumption, we can identify where you are simply burning your money. We can suggest and implement easy solutions to save you money and minimise your carbon emmissions.</p>
  </section>

  <blockquote class="abs quote">
    <svg width="32" height="24" viewBox="0 0 32 24"><path d="M2 22V12C2 5 6 2 12 2v5c-3 0-5 2-5 5h5v10zM18 22V12c0-7 4-10 10-10v5c-3 0-5 2-5 5h5v10z" fill="#c8c8c8"/></svg>
    <p>Brivol Electric considerd all our needs and incorparated energy saving into the project....</p>
    <cite>- Sam Carter, <span>Lumen Agency</span></cite>
  </blockquote>

  <div class="abs foot-line"></div>
  <div class="abs foot-links">Home<span>|</span>About<span>|</span>Services<span>|</span>Our Work<span>|</span>Specials<span>|</span>Energy Efficiency<span>|</span>Contact</div>
  <div class="abs copy">Copyright © 2013 brivolelectric.com.au. <a>Privacy Policy</a></div>
</main>
</body>
</html>
```